Birchwood Turf Care_2015 New Cards_V1

We need an enhanced business card from what we have today. We are a Landscaping company and we have an existing Logo and text info that we would like to include.
Text to include:
In business for over 20 years,Fully Insured, Weekly Lawn Maintenance, Spring & Fall Clean-up, Dale Whitford, 203-555-0147, www.birchwoodturfcarect.example, Visit our Website for additional Lawn Care Services or email directly at DALE@BIRCHWOODTURFCARE.EXAMPLE, We appreciate your business.
We want full color background and we will want to take this design and work with a printer that does high graphic silk screen cards. The colors we have thought about are Black, with our Green Logo, with Gold Text...we are open to different colors, we just want the card to wow!

Target Market(s)

Lawn Care Maintenance

Industry/Entity Type

Lawn Care

Contact Information for Business Card

Text to include:
In business for over 20 years, Fully Insured, Weekly Lawn Maintenance, Spring & Fall Clean-up, Dale Whitford, 203-555-0147, www.birchwoodturfcarect.example, Visit our Website for additional Lawn Care Services or email directly at DALE@BIRCHWOODTURFCARE.EXAMPLE, We appreciate your business.

Requirements
Must have
• Logo, text details about how to reach us, standard size business cards that go horizontal.
Nice to have
• background colors, background designs, raised embossed lettering, rounded corners(2 or 4),

```html
<!DOCTYPE html>
<html lang="en">
<head>
<meta charset="utf-8">
<title>Birchwood Turf Care – Business Card</title>
<link href="https://fonts.googleapis.com/css2?family=Encode+Sans+Semi+Condensed:wght@600&family=Questrial&display=swap" rel="stylesheet">
<style>
  :root {
    --page-bg: #1c1c1c;
    --card-white: #ffffff;
    --brand-dark: #0f3a12;
    --brand-green: #2e7d1e;
    --leaf-green: #6ab534;
    --text-dark: #2b2b2b;
    --back-top: #052208;
    --back-bottom: #1b4b16;
    --text-light: #f2f2f2;
  }
  * { margin: 0; padding: 0; box-sizing: border-box; }
  html, body { width: 1200px; height: 1001px; overflow: hidden; }
  body {
    background: var(--page-bg);
    font-family: "Questrial", sans-serif;
    position: relative;
  }
  .card {
    position: absolute;
    left: 306px;
    width: 587px;
    height: 329px;
    border-radius: 14px;
    overflow: hidden;
  }
  .card-front { top: 133px; background: var(--card-white); }
  .card-back {
    top: 540px;
    background: linear-gradient(180deg, var(--back-top) 0%, var(--back-bottom) 100%);
    text-align: center;
    color: var(--text-light);
  }

  /* front */
  .brand-name {
    position: absolute;
    font-family: "Encode Sans Semi Condensed", sans-serif;
    font-weight: 600;
    text-transform: uppercase;
    line-height: 0.95;
  }
  .card-front .brand-name {
    left: 56px; top: 62px; width: 220px;
    color: var(--brand-dark);
    font-size: 40px;
    text-align: center;
  }
  .contact-name {
    position: absolute; left: 310px; top: 60px;
    font-family: "Encode Sans Semi Condensed", sans-serif;
    font-weight: 600; font-size: 21px;
    color: var(--brand-green);
    letter-spacing: 0.3px;
  }
  .contact-list {
    position: absolute; left: 310px; top: 95px;
    list-style: none;
    font-size: 15.5px; color: var(--text-dark);
  }
  .contact-list li {
    display: flex; align-items: center; gap: 9px;
    height: 20px;
  }
  .contact-list svg { width: 15px; height: 15px; flex: none; }
  .services {
    position: absolute; left: 0; right: 0; top: 200px;
    text-align: center;
    font-size: 14.5px; line-height: 18px; color: var(--text-dark);
  }
  .grass-band {
    position: absolute; left: 0; bottom: 0;
    width: 100%; height: 70px;
  }

  /* back */
  .card-back .brand-name {
    left: 0; right: 0; top: 52px;
    color: var(--text-light);
    font-size: 58px;
  }
  .website {
    position: absolute; left: 0; right: 0; top: 211px;
    font-size: 15.5px;
  }
  .website .domain { color: var(--leaf-green); }
  .note {
    position: absolute; left: 0; right: 0; top: 253px;
    font-size: 14.5px; line-height: 18px;
  }
</style>
</head>
<body>

<section class="card card-front">
  <div class="brand-name">Birchwood<br>Turf Care</div>

  <h1 class="contact-name">DALE WHITFORD</h1>
  <ul class="contact-list">
    <li>
      <svg viewBox="0 0 16 16" aria-hidden="true"><rect width="16" height="16" rx="3" fill="#2e7d1e"/><path d="M5 3.5l2 .3.6 2.3-1.2.9a6 6 0 0 0 2.6 2.6l.9-1.2 2.3.6.3 2-1.4 1.2C7.8 12 4 8.2 3.8 4.9z" fill="#fff"/></svg>
      203-555-0147
    </li>
    <li>
      <svg viewBox="0 0 16 16" aria-hidden="true"><rect width="16" height="16" rx="3" fill="#2e7d1e"/><rect x="3" y="4.5" width="10" height="7" fill="none" stroke="#fff" stroke-width="1.2"/><path d="M3 4.5l5 4 5-4" fill="none" stroke="#fff" stroke-width="1.2"/></svg>
      dale@birchwoodturfcarect.example
    </li>
    <li>
      <svg viewBox="0 0 16 16" aria-hidden="true"><rect width="16" height="16" rx="3" fill="#2e7d1e"/><circle cx="8" cy="8" r="4.8" fill="none" stroke="#fff" stroke-width="1.1"/><ellipse cx="8" cy="8" rx="2" ry="4.8" fill="none" stroke="#fff" stroke-width="1"/><path d="M3.2 8h9.6" stroke="#fff" stroke-width="1"/></svg>
      www.birchwoodturfcarect.example
    </li>
  </ul>

  <p class="services">In business for over 20 years · Fully Insured<br>Weekly Lawn Maintenance · Spring &amp; Fall Clean-up</p>

  <svg class="grass-band" viewBox="0 0 587 70" preserveAspectRatio="none" role="img" aria-label="Grass silhouette with a rolling green hill">
    <defs>
      <linearGradient id="grassFill" x1="0" y1="0" x2="0" y2="1">
        <stop offset="0" stop-color="#1e5a17"/>
        <stop offset="1" stop-color="#2f7a22"/>
      </linearGradient>
    </defs>
    <rect width="587" height="70" fill="url(#grassFill)"/>
  </svg>
</section>

<section class="card card-back">
  <div class="brand-name">Birchwood Turf Care</div>
  <p class="website">www.<span class="domain">birchwoodturfcarect</span>.example</p>
  <p class="note">Visit our website for additional Lawn Care Services or email<br>directly at dale@birchwoodturfcare.example We appreciate your business.</p>
</section>

</body>
</html>
```